New Business Card Design Project

Looking for a modern business card design for an import distribution business for industrial technical products. The winning design will translate modern, sophistication, technical, professional and sustainable.

Target Market(s)

Technical customers

Industry/Entity Type

Business

Contact Information for Business Card

Dean Harlow
Sales Manager
M: 0471 625 183
P: 1300 872 619
dean@volkarsystems.com.au
4/18 Galloway Crest Road
Marlow Heights NSW 2163
www.volkarsystems.com.au

Font styles to use
Sans Serif

Colors
ec1f27
606060
000000
fbfbfb

Requirements
Must have
• My Logo which is the Volkar Systems logo attached
Nice to have
• Eurostile Bold font

```html
<!DOCTYPE html>
<html lang="en">
<head>
<meta charset="utf-8">
<title>Volkar Systems – Business Card</title>
<link rel="stylesheet" href="https://fonts.googleapis.com/css2?family=Saira:wght@400;600;700&display=swap">
<style>
  :root {
    --brand-red: #bd2a24;
    --ink-grey: #5f6266;
    --card-white: #f3f3f3;
    --soft-white: #e6e6e6;
    --backdrop: #8f8f8f;
    --rule-grey: #77797c;
  }
  * { margin: 0; padding: 0; box-sizing: border-box; }
  html, body {
    width: 1105px; height: 1200px; overflow: hidden;
    background: var(--backdrop);
    font-family: "Saira", Arial, sans-serif;
  }
  .canvas { position: relative; width: 1105px; height: 1200px; }
  .card {
    position: absolute; left: 182px; width: 746px; height: 426px; overflow: hidden;
  }
  .card--front { top: 120px; background: var(--card-white); }
  .card--back { top: 637px; background: var(--brand-red); }

  .brand {
    position: absolute; left: 144px; top: 84px;
    display: flex; align-items: center; gap: 20px;
  }
  .brand__square { width: 76px; height: 76px; background: var(--brand-red); }
  .brand__name {
    font-weight: 700; font-size: 40px; letter-spacing: 2px;
    color: var(--brand-red); text-transform: uppercase; line-height: 1;
  }

  .identity {
    position: absolute; right: calc(746px - 312px); top: 204px;
    text-align: right; color: var(--ink-grey); font-size: 19px; line-height: 29px;
    white-space: nowrap;
  }
  .identity__name {
    color: var(--brand-red); font-weight: 600; font-size: 28px; line-height: 34px;
  }
  .divider {
    position: absolute; left: 341px; top: 204px; width: 1px; height: 118px;
    background: #b9b9b9;
  }
  .contacts {
    position: absolute; left: 374px; top: 208px; list-style: none;
    color: var(--ink-grey); font-size: 19px; white-space: nowrap;
  }
  .contacts li { display: flex; align-items: center; height: 30px; }
  .contacts svg { width: 17px; height: 17px; margin-right: 10px; fill: var(--brand-red); }

  .card__rule {
    position: absolute; left: 0; right: 0; top: 388px; height: 4px; background: var(--rule-grey);
  }
  .card__band {
    position: absolute; left: 0; right: 0; top: 396px; bottom: 0; background: var(--brand-red);
  }

  .back-brand {
    position: absolute; left: 0; right: 0; top: 150px;
    display: flex; align-items: center; justify-content: center; gap: 18px;
  }
  .back-brand__square { width: 60px; height: 60px; background: var(--soft-white); }
  .back-brand__name {
    font-weight: 700; font-size: 50px; letter-spacing: 2px;
    color: var(--soft-white); text-transform: uppercase; line-height: 1;
  }
  .back-url {
    position: absolute; left: 0; right: 0; top: 354px; text-align: center;
    color: var(--soft-white); font-size: 19px; letter-spacing: 2px;
  }
</style>
</head>
<body>
<main class="canvas">
  <section class="card card--front">
    <div class="brand">
      <span class="brand__square"></span>
      <span class="brand__name">Volkar Systems</span>
    </div>

    <div class="identity">
      <p class="identity__name">Dean Harlow</p>
      <p>Sales Manager</p>
      <p>4/18 Galloway Crest Road</p>
      <p>Marlow Heights NSW 2163</p>
    </div>

    <span class="divider"></span>

    <ul class="contacts">
      <li>
        <svg viewBox="0 0 24 24"><path d="M6.6 10.8a15 15 0 0 0 6.6 6.6l2.2-2.2c.3-.3.7-.4 1-.2 1.1.4 2.3.6 3.6.6.6 0 1 .4 1 1V20c0 .6-.4 1-1 1A17 17 0 0 1 3 4c0-.6.4-1 1-1h3.5c.6 0 1 .4 1 1 0 1.3.2 2.5.6 3.6.1.3 0 .7-.2 1z"/></svg>
        1300 872 619
      </li>
      <li>
        <svg viewBox="0 0 24 24"><path d="M7 1h10a2 2 0 0 1 2 2v18a2 2 0 0 1-2 2H7a2 2 0 0 1-2-2V3a2 2 0 0 1 2-2zm0 3v14h10V4zm5 15.5a1.2 1.2 0 1 0 0 2.4 1.2 1.2 0 0 0 0-2.4z"/></svg>
        0471 625 183
      </li>
      <li>
        <svg viewBox="0 0 24 24"><path d="M2 5h20v14H2zm2 2v.4l8 5.2 8-5.2V7zm0 2.8V17h16V9.8l-8 5.2z"/></svg>
        dean@volkarsystems.com.au
      </li>
      <li>
        <svg viewBox="0 0 24 24"><path d="M12 2a10 10 0 1 0 0 20 10 10 0 0 0 0-20zm-1 17.9A8 8 0 0 1 4.2 10.3L9 15v1a2 2 0 0 0 2 2zm6.9-2.5A2 2 0 0 0 16 16h-1v-3a1 1 0 0 0-1-1H8v-2h2a1 1 0 0 0 1-1V7h2a2 2 0 0 0 2-2v-.4a8 8 0 0 1 2.9 12.8z"/></svg>
        www.volkarsystems.com.au
      </li>
    </ul>

    <span class="card__rule"></span>
    <span class="card__band"></span>
  </section>

  <section class="card card--back">
    <div class="back-brand">
      <span class="back-brand__square"></span>
      <span class="back-brand__name">Volkar Systems</span>
    </div>
    <p class="back-url">www.volkarsystems.com.au</p>
  </section>
</main>
</body>
</html>
```